Responsive OnePage Design for recruitment company

BrightHire is a modern company that sources interim people for its customers. Mostly developers, scrum master, project managers and designers. In this website we want to tell something about us, about how we work, our customers and we want our candidates be able to subscribe. The subscription form should be several fields (name, surname, email address, phone number and the possibility to upload your resume.We want it to fit into a existing wordpress plugin. We also want a listing of our job opportunities. The listing should be designed in a clear readable overview and if you click on the job you should get the details and be able to respond quickly by filling in you name, surname, email address, rate, phone number and upload your resume. We want this to be a standard configurable plugin. It should be easy to fill in the jobs in Wordpress by our administrator. We want a fresh, modern and cool design. It should be a responsive onepage design. If you click on a listed job you should stay on the same page. Our logo is added.

Target Market(s)

recruitment

Industry/Entity Type

Recruitment

Font styles to use
Sans Serif

Colors

Designer to choose colors to be used in the design.

Requirements
Must have
• Onepage design
• listing of job opportunities
• subscription forms
• be responsive

```html
<!DOCTYPE html>
<html lang="en">
<head>
<meta charset="utf-8">
<title>BrightHire – One Page Recruitment Site</title>
<link rel="stylesheet" href="https://fonts.googleapis.com/css2?family=Roboto:wght@400;500;700&display=swap">
<style>
:root{
  --blue:#0b6fbf;
  --blue-dark:#085a9c;
  --ink:#2c2c2c;
  --muted:#8a8a8a;
  --page-bg:#e6e6e6;
  --white:#ffffff;
  --footer:#5b5b5b;
  --btn-grey:#555555;
  --card-bg:#f7f9fb;
  --line:#dfe4ea;
}
*{box-sizing:border-box;margin:0;padding:0}
html,body{width:817px;height:1200px;overflow:hidden;background:var(--page-bg);font-family:"Roboto",Arial,sans-serif;color:var(--ink)}
.stage{position:absolute;left:0;top:0;width:1021px;height:1500px;transform:scale(.8);transform-origin:0 0}
.page{position:absolute;background:var(--white);overflow:hidden}
.page section,.page header,.page footer{position:relative;overflow:hidden}
.abs{position:absolute}
.blue{color:var(--blue)}
.wordmark{font-weight:500;color:var(--ink);letter-spacing:0}
.btn{position:absolute;background:var(--blue);color:#fff;font-weight:700;text-align:center;letter-spacing:.3px;white-space:nowrap}
.btn.grey{background:var(--btn-grey)}
.field{position:absolute;border:1px solid rgba(255,255,255,.8);color:#fff;font-style:italic}
.photo-city{background:linear-gradient(180deg,#d9dde2 0%,#b8bfc6 35%,#8e979f 70%,#6d757c 100%)}
.photo-office{background:linear-gradient(120deg,#cfd6d9 0%,#a9b2b2 40%,#7d6f66 75%,#5b4f48 100%)}
.circle{position:absolute;border-radius:50%;background:#fff;border:2px solid #cfe1f1;display:flex;align-items:center;justify-content:center}
.avatar{position:absolute;border-radius:50%;border:3px solid var(--blue);background:linear-gradient(180deg,#c9cdd2,#8f979e)}

/* ---------- desktop ---------- */
.desk{left:151px;top:27px;width:458px;height:1438px}
.desk .top-bar{height:27px}
.desk .logo{position:absolute;left:0;right:0;top:8px;text-align:center;font-size:11px}
.desk .hero{height:238px}
.desk .hero h1{position:absolute;left:0;right:0;top:48px;text-align:center;font-size:24px;font-weight:700;color:var(--blue);line-height:1}
.desk .hero h2{position:absolute;left:0;right:0;top:73px;text-align:center;font-size:12px;font-weight:500;color:#1e1e1e}
.desk .search{height:50px;background:var(--blue)}
.desk .input{position:absolute;top:9px;height:20px;background:#fff;font-size:5px;color:#aaa;font-style:italic;padding:7px 8px}
.desk .about{height:110px;text-align:center}
.desk .sec-title{font-size:10px;font-weight:500;letter-spacing:.4px}
.desk .how{height:196px;background:var(--blue);color:#fff}
.desk .step{position:absolute;top:57px;width:80px;text-align:center}
.desk .step .circle{position:relative;margin:0 auto;width:62px;height:62px}
.desk .step b{display:block;margin-top:8px;font-size:10px;font-weight:500}
.desk .step p{font-size:4.6px;line-height:1.35;margin-top:2px;padding:0 6px}
.desk .jobs{height:332px}
.job{position:absolute;left:36px;width:385px;height:66px;background:var(--card-bg);box-shadow:0 0 3px rgba(0,0,0,.15)}
.job .title{position:absolute;left:15px;top:10px;font-size:10px;color:var(--blue);font-weight:500}
.job .role{position:absolute;left:15px;top:25px;font-size:6.5px;color:#666}
.job .meta{position:absolute;left:15px;top:46px;font-size:4.5px;color:#888;display:flex;gap:22px}
.job .side{position:absolute;right:0;top:0;width:104px;height:66px;background:#fff}
.job .btn{left:20px;width:62px;height:14px;font-size:4.5px;line-height:14px}
.desk .subscribe{height:160px;background:var(--blue)}
.desk .candidates{height:188px;text-align:center}
.cand-name{position:absolute;width:60px;text-align:center;font-size:5px}
.cand-name span{display:block;color:var(--blue)}
.desk footer{height:137px;background:var(--footer);color:#fff}
.desk footer h4{position:absolute;top:24px;font-size:10px;font-weight:500}
.desk footer .list{position:absolute;top:45px;font-size:4.8px;line-height:1.4}

/* ---------- mobile ---------- */
.mob{left:659px;top:45px;width:159px;height:1395px}
.mob .top-bar{height:25px}
.mob .hero{height:147px}
.mob .hero h1{position:absolute;left:0;right:0;top:29px;text-align:center;font-size:14px;font-weight:700;color:var(--blue);line-height:1}
.mob .hero h2{position:absolute;left:0;right:0;top:44px;text-align:center;font-size:7px;font-weight:500}
.mob .search{height:45px;background:var(--blue)}
.mob .input{position:absolute;left:8px;width:144px;height:10px;background:#fff;font-size:3px;color:#aaa;padding:3px 5px}
.mob .how{height:403px;background:var(--blue);color:#fff;text-align:center}
.mob .mstep{position:absolute;left:0;right:0;text-align:center}
.mob .mstep .circle{position:relative;margin:0 auto;width:40px;height:40px}
.mob .mstep b{display:block;font-size:6px;font-weight:500;margin-top:3px}
.mob .mstep p{font-size:2.6px;line-height:1.35;width:40px;margin:1px auto 0}
.mjob{position:absolute;left:8px;width:144px;height:76px;background:var(--card-bg);box-shadow:0 0 2px rgba(0,0,0,.15)}
.mjob .t{position:absolute;left:8px;top:7px;font-size:6px;color:var(--blue);font-weight:500}
.mjob .r{position:absolute;left:8px;top:15px;font-size:3.5px;color:#666}
.mjob .m{position:absolute;left:8px;top:27px;font-size:2.6px;color:#888;word-spacing:4px}
.mjob .btn{left:52px;width:39px;height:9px;font-size:2.6px;line-height:9px}
.mob footer{height:112px;background:var(--footer);color:#fff}
</style>
</head>
<body>
<div class="stage">

  <!-- ================= DESKTOP ================= -->
  <main class="page desk">
    <header class="top-bar">
      <svg class="abs" style="left:37px;top:10px" width="11" height="8" viewBox="0 0 11 8"><path d="M0 1h11M0 4h11M0 7h8" stroke="#333" stroke-width="1.2"/></svg>
      <div class="logo wordmark">BrightHire</div>
      <div class="abs" style="right:36px;top:10px;font-size:5px;color:#555">▢ Login &nbsp;|&nbsp; <span class="blue">⚲ Register</span></div>
    </header>

    <section class="hero photo-city" role="img" aria-label="Businessman standing on a rooftop looking out over a city skyline">
      <h1>YOUR GATEWAY</h1>
      <h2>TO A BETTER FUTURE</h2>
    </section>

    <section class="search">
      <div class="input" style="left:37px;width:175px">Job title, Keywords or Company name</div>
      <div class="input" style="left:217px;width:177px">City, Province or region</div>
      <div class="abs" style="left:396px;top:9px;width:25px;height:20px;background:var(--btn-grey)">
        <svg width="25" height="20" viewBox="0 0 25 20"><circle cx="11.5" cy="9" r="3.5" fill="none" stroke="#fff" stroke-width="1.3"/><path d="M14 11.5l3 3" stroke="#fff" stroke-width="1.3"/></svg>
      </div>
      <div class="abs" style="left:37px;top:33px;font-size:5px;color:#fff;font-style:italic">Or browse jobs offer by <span style="border:1px solid #fff;padding:1px 5px;font-style:normal">Category</span></div>
    </section>

    <section class="about">
      <div class="sec-title" style="margin-top:21px">ABOUT <span class="blue">US</span></div>
      <p style="font-size:4.8px;line-height:1.35;width:256px;margin:14px auto 0">Lorem Ipsum is simply dummy text of the printing and typesetting industry. Lorem Ipsum has been the industry's standard dummy text ever since the 1500s, when an unknown printer took a galley of type and scrambled it to make a type specimen book.</p>
      <div class="btn" style="left:198px;top:76px;width:63px;height:16px;font-size:4.5px;line-height:16px">READ MORE</div>
    </section>

    <section class="how">
      <div class="sec-title" style="text-align:center;margin-top:26px;letter-spacing:1.4px">HOW WE WORK</div>
      <div class="step" style="left:29px"><div class="circle"><svg width="26" height="26" viewBox="0 0 26 26" fill="none" stroke="#555" stroke-width="1"><circle cx="13" cy="13" r="4"/><circle cx="13" cy="3" r="2"/><circle cx="13" cy="23" r="2"/><circle cx="4" cy="8" r="2"/><circle cx="22" cy="8" r="2"/><circle cx="4" cy="18" r="2"/><circle cx="22" cy="18" r="2"/><path d="M13 5v4M13 17v4M6 9l4 2M20 9l-4 2M6 17l4-2M20 17l-4-2"/></svg></div><b>Connect</b><p>Lorem Ipsum is simply dummy text of the printing and typesetting industry.</p></div>
      <div class="step" style="left:109px"><div class="circle"><svg width="26" height="26" viewBox="0 0 26 26" fill="none" stroke="#555" stroke-width="1"><rect x="4" y="3" width="13" height="18"/><path d="M7 7h7M7 10h4M7 13h4"/><circle cx="18" cy="15" r="4"/></svg></div><b>Analyze</b><p>Lorem Ipsum is simply dummy text of the printing and typesetting industry.</p></div>
      <div class="step" style="left:189px"><div class="circle"><svg width="26" height="26" viewBox="0 0 26 26" fill="none" stroke="#333" stroke-width="1.5"><circle cx="11" cy="11" r="6"/><path d="M15.5 15.5l6 6"/></svg></div><b>Search</b><p>Lorem Ipsum is simply dummy text of the printing and typesetting industry.</p></div>
      <div class="step" style="left:269px"><div class="circle"><svg width="26" height="26" viewBox="0 0 26 26" fill="none" stroke="#555" stroke-width="1"><circle cx="13" cy="10" r="6"/><circle cx="13" cy="10" r="3"/><path d="M9 15l-2 8 3-2 2 3M17 15l2 8-3-2-2 3"/></svg></div><b>Rank</b><p>Lorem Ipsum is simply dummy text of the printing and typesetting industry.</p></div>
      <div class="step" style="left:349px"><div class="circle"><svg width="26" height="26" viewBox="0 0 26 26" fill="none" stroke="#555" stroke-width="1"><path d="M3 11l10-7 10 7v11H3z"/><path d="M3 11l10 7 10-7"/><path d="M7 9h12M8 12h10"/></svg></div><b>Deliver</b><p>Lorem Ipsum is simply dummy text of the printing and typesetting industry.</p></div>
    </section>

    <section class="jobs">
      <div class="sec-title abs" style="left:37px;top:40px">FEATURE <span class="blue">JOBS</span></div>
      <article class="job" style="top:63px"><div class="title">Job Title</div><div class="role">◇ Scrum Master</div><div class="meta"><span>▢ Part-Time</span><span>⚲ China</span><span>⇄ Up to $ 35000+Commission</span><span>◷ 8:00 AM to 5:00 PM</span></div><div class="side"><div class="btn grey" style="top:17px">FULL DETAIL</div><div class="btn" style="top:36px">QUICK INQUIRY</div></div></article>
      <article class="job" style="top:136px"><div class="title">Job Title</div><div class="role">◇ Project Manager</div><div class="meta"><span>▢ Full-Time</span><span>⚲ USA</span><span>⇄ Up to $ 55000+Commission</span><span>◷ 8:00 AM to 5:00 PM</span></div><div class="side"><div class="btn" style="top:15px">FULL DETAIL</div><div class="btn" style="top:34px">QUICK INQUIRY</div></div></article>
      <article class="job" style="top:208px"><div class="title">Job Title</div><div class="role">◇ Designer</div><div class="meta"><span>▢ Full-Time</span><span>⚲ USA</span><span>⇄ Up to $ 30000+Commission</span><span>◷ 8:00 AM to 5:00 PM</span></div><div class="side"><div class="btn" style="top:16px">FULL DETAIL</div><div class="btn" style="top:35px">QUICK INQUIRY</div></div></article>
      <div class="btn" style="left:198px;top:297px;width:63px;height:16px;font-size:4.5px;line-height:16px">VIEW ALL JOBS</div>
    </section>

    <section class="subscribe">
      <div class="abs photo-office" style="left:0;top:0;width:225px;height:160px" role="img" aria-label="Smiling woman working on a laptop at a desk by a window"></div>
      <div class="abs" style="left:225px;right:0;top:16px;text-align:center;color:#fff;font-size:10px;font-weight:500;letter-spacing:1.4px">SUBSCRIBE</div>
      <div class="field" style="left:253px;top:38px;width:82px;height:16px;font-size:4.5px;padding:5px 4px">Your name</div>
      <div class="field" style="left:339px;top:38px;width:84px;height:16px;font-size:4.5px;padding:5px 4px">Your surname</div>
      <div class="field" style="left:253px;top:58px;width:82px;height:16px;font-size:4.5px;padding:5px 4px">Email address</div>
      <div class="field" style="left:339px;top:58px;width:84px;height:16px;font-size:4.5px;padding:5px 4px">Phone#</div>
      <div class="field" style="left:253px;top:78px;width:170px;height:40px;font-size:4.5px;padding:5px 4px">Message
        <span class="abs" style="right:5px;bottom:5px;background:var(--btn-grey);font-style:normal;font-size:3px;padding:2px 4px">Upload Resume ⇪</span></div>
      <div class="btn grey" style="left:253px;top:124px;width:62px;height:16px;font-size:4.5px;line-height:16px">SUBSCRIBE</div>
    </section>

    <section class="candidates">
      <div class="sec-title" style="margin-top:25px;letter-spacing:1.4px">FEATURE <span class="blue">CANDIDATES</span></div>
      <svg class="abs" style="left:15px;top:74px" width="13" height="13" viewBox="0 0 13 13" fill="none" stroke="#777"><circle cx="6.5" cy="6.5" r="6"/><path d="M8 4L5.5 6.5 8 9"/></svg>
      <svg class="abs" style="left:431px;top:74px" width="13" height="13" viewBox="0 0 13 13" fill="none" stroke="var(--blue)"><circle cx="6.5" cy="6.5" r="6"/><path d="M5 4l2.5 2.5L5 9"/></svg>
      <div class="avatar" style="left:47px;top:56px;width:50px;height:50px" role="img" aria-label="Candidate portrait"></div>
      <div class="avatar" style="left:109px;top:56px;width:50px;height:50px" role="img" aria-label="Candidate portrait"></div>
      <div class="avatar" style="left:172px;top:56px;width:50px;height:50px" role="img" aria-label="Candidate portrait"></div>
      <div class="avatar" style="left:235px;top:56px;width:50px;height:50px" role="img" aria-label="Candidate portrait"></div>
      <div class="avatar" style="left:298px;top:56px;width:50px;height:50px" role="img" aria-label="Candidate portrait"></div>
      <div class="avatar" style="left:361px;top:56px;width:50px;height:50px" role="img" aria-label="Candidate portrait"></div>
      <div class="cand-name" style="left:42px;top:119px">Liam Carter<span>Designation</span></div>
      <div class="cand-name" style="left:104px;top:119px">Noah Patel<span>Designation</span></div>
      <div class="cand-name" style="left:167px;top:119px">Evan Brooks<span>Designation</span></div>
      <div class="cand-name" style="left:230px;top:119px">Owen Hale<span>Designation</span></div>
      <div class="cand-name" style="left:293px;top:119px">Mark Dale<span>Designation</span></div>
      <div class="cand-name" style="left:356px;top:119px">Adam Reeve<span>Designation</span></div>
      <div class="btn" style="left:192px;top:153px;width:75px;height:16px;font-size:4.5px;line-height:16px">VIEW ALL CANDIDATES</div>
    </section>

    <footer>
      <div class="abs" style="left:37px;top:23px;font-size:9px;font-weight:500">BrightHire</div>
      <p class="abs" style="left:37px;top:43px;width:86px;font-size:4.8px;line-height:1.3">Lorem Ipsum is simply dummy text of the printing and typesetting industry. Lorem Ipsum has been the industry's standard dummy text ever since the 1500s.</p>
      <svg class="abs" style="left:37px;top:78px" width="76" height="8" viewBox="0 0 76 8" fill="#fff"><circle cx="4" cy="4" r="3"/><circle cx="19" cy="4" r="3"/><circle cx="34" cy="4" r="3"/><circle cx="49" cy="4" r="3"/><circle cx="64" cy="4" r="3"/></svg>
      <h4 style="left:154px">Quick Links</h4>
      <div class="list" style="left:158px">Home<br>About us<br>How We Work<br>Jobs<br>Candidates<br>Subscribe<br>Contact us</div>
      <h4 style="left:247px">Useful Info..</h4>
      <div class="list" style="left:255px">(+000) 555 0101<br>(+000) 555 0102<br>(+000) 555 0103<br>info@brighthire.example<br>48 Elm Street<br>Fairview</div>
      <h4 style="left:337px">Contact us</h4>
      <div class="field" style="left:338px;top:44px;width:42px;height:10px;font-size:3.5px;padding:2px 3px">Full Name</div>
      <div class="field" style="left:382px;top:44px;width:40px;height:10px;font-size:3.5px;padding:2px 3px">Email</div>
      <div class="field" style="left:338px;top:56px;width:84px;height:18px;font-size:3.5px;padding:2px 3px">Message</div>
      <div class="btn" style="left:338px;top:77px;width:42px;height:8px;font-size:3px;line-height:8px">SUBMIT NOW</div>
      <div class="abs" style="left:37px;right:37px;top:99px;border-top:1px solid rgba(255,255,255,.4)"></div>
      <div class="abs" style="left:37px;top:108px;font-size:4.2px">Copyright © 2019 BrightHire, All Rights Reserved</div>
      <div class="abs" style="right:37px;top:108px;font-size:4.2px">Privacy Policy · Terms &amp; Conditions</div>
    </footer>
  </main>

  <!-- ================= MOBILE ================= -->
  <main class="page mob">
    <header class="top-bar">
      <div class="abs" style="right:4px;top:4px;font-size:2.6px;color:#555">Login | <span class="blue">Register</span></div>
      <svg class="abs" style="left:8px;top:14px" width="6" height="5" viewBox="0 0 6 5"><path d="M0 .5h6M0 2.5h6M0 4.5h4" stroke="#333" stroke-width=".8"/></svg>
      <div class="abs wordmark" style="left:0;right:0;top:12px;text-align:center;font-size:6.5px">BrightHire</div>
    </header>
    <section class="hero photo-city" role="img" aria-label="Businessman standing on a rooftop looking out over a city skyline">
      <h1>YOUR GATEWAY</h1><h2>TO A BETTER FUTURE</h2>
    </section>
    <section class="search">
      <div class="input" style="top:6px">Job title, Keywords or Company name</div>
      <div class="input" style="top:19px">City, Province or region</div>
      <div class="abs" style="left:8px;top:33px;font-size:2.6px;color:#fff">Or browse jobs offer by <span style="border:1px solid #fff;padding:0 2px">Category</span></div>
      <div class="abs" style="left:140px;top:33px;width:12px;height:9px;background:var(--btn-grey)">
        <svg width="12" height="9" viewBox="0 0 12 9"><circle cx="5.5" cy="4" r="1.8" fill="none" stroke="#fff" stroke-width=".7"/><path d="M6.8 5.3l1.5 1.5" stroke="#fff" stroke-width=".7"/></svg>
      </div>
    </section>
    <section style="height:68px;text-align:center">
      <div style="font-size:6px;font-weight:500;margin-top:14px">ABOUT <span class="blue">US</span></div>
      <p style="font-size:2.6px;line-height:1.35;width:130px;margin:8px auto 0">Lorem Ipsum is simply dummy text of the printing and typesetting industry. Lorem Ipsum has been the industry's standard dummy text ever since the 1500s, when an unknown printer took a galley of type and scrambled it to make a type specimen book.</p>
      <div class="btn" style="left:60px;top:47px;width:39px;height:9px;font-size:2.6px;line-height:9px">READ MORE</div>
    </section>
    <section class="how">
      <div style="font-size:5.5px;letter-spacing:1px;font-weight:500;margin-top:15px">HOW WE WORK</div>
      <div class="mstep" style="top:30px"><div class="circle"><svg width="16" height="16" viewBox="0 0 26 26" fill="none" stroke="#555" stroke-width="1.3"><circle cx="13" cy="13" r="4"/><circle cx="13" cy="3" r="2"/><circle cx="13" cy="23" r="2"/><circle cx="4" cy="8" r="2"/><circle cx="22" cy="8" r="2"/><circle cx="4" cy="18" r="2"/><circle cx="22" cy="18" r="2"/><path d="M13 5v4M13 17v4M6 9l4 2M20 9l-4 2M6 17l4-2M20 17l-4-2"/></svg></div><b>Connect</b><p>Lorem Ipsum is simply dummy text of the printing and typesetting industry.</p></div>
      <div class="mstep" style="top:105px"><div class="circle"><svg width="16" height="16" viewBox="0 0 26 26" fill="none" stroke="#555" stroke-width="1.3"><rect x="4" y="3" width="13" height="18"/><path d="M7 7h7M7 10h4M7 13h4"/><circle cx="18" cy="15" r="4"/></svg></div><b>Analyze</b><p>Lorem Ipsum is simply dummy text of the printing and typesetting industry.</p></div>
      <div class="mstep" style="top:179px"><div class="circle"><svg width="14" height="14" viewBox="0 0 26 26" fill="none" stroke="#333" stroke-width="2"><circle cx="11" cy="11" r="6"/><path d="M15.5 15.5l6 6"/></svg></div><b>Search</b><p>Lorem Ipsum is simply dummy text of the printing and typesetting industry.</p></div>
      <div class="mstep" style="top:254px"><div class="circle"><svg width="16" height="16" viewBox="0 0 26 26" fill="none" stroke="#555" stroke-width="1.3"><circle cx="13" cy="10" r="6"/><circle cx="13" cy="10" r="3"/><path d="M9 15l-2 8 3-2 2 3M17 15l2 8-3-2-2 3"/></svg></div><b>Rank</b><p>Lorem Ipsum is simply dummy text of the printing and typesetting industry.</p></div>
      <div class="mstep" style="top:326px"><div class="circle"><svg width="16" height="16" viewBox="0 0 26 26" fill="none" stroke="#555" stroke-width="1.3"><path d="M3 11l10-7 10 7v11H3z"/><path d="M3 11l10 7 10-7"/><path d="M7 9h12M8 12h10"/></svg></div><b>Deliver</b><p>Lorem Ipsum is simply dummy text of the printing and typesetting industry.</p></div>
    </section>
    <section style="height:297px">
      <div class="abs" style="left:8px;top:12px;font-size:5.5px;font-weight:500">FEATURE <span class="blue">JOBS</span></div>
      <article class="mjob" style="top:27px"><div class="t">Job Title</div><div class="r">◇ Scrum Master</div><div class="m">Part-Time China $35000+Commission 8:00 AM to 5:00 PM</div><div class="btn grey" style="top:46px">FULL DETAIL</div><div class="btn" style="top:59px">QUICK INQUIRY</div></article>
      <article class="mjob" style="top:107px"><div class="t">Job Title</div><div class="r">◇ Scrum Master</div><div class="m">Full-Time USA $55000+Commission 8:00 AM to 5:00 PM</div><div class="btn" style="top:44px">FULL DETAIL</div><div class="btn" style="top:57px">QUICK INQUIRY</div></article>
      <article class="mjob" style="top:187px"><div class="t">Job Title</div><div class="r">◇ Scrum Master</div><div class="m">Full-Time USA $30000+Commission 8:00 AM to 5:00 PM</div><div class="btn" style="top:45px">FULL DETAIL</div><div class="btn" style="top:59px">QUICK INQUIRY</div></article>
      <div class="btn" style="left:60px;top:276px;width:39px;height:9px;font-size:2.6px;line-height:9px">VIEW ALL JOBS</div>
    </section>
    <section class="photo-office" style="height:98px" role="img" aria-label="Smiling woman working on a laptop at a desk by a window"></section>
    <section style="height:100px;background:var(--blue)">
      <div class="abs" style="left:0;right:0;top:10px;text-align:center;color:#fff;font-size:6px;letter-spacing:1px;font-weight:500">SUBSCRIBE</div>
      <div class="field" style="left:28px;top:24px;width:50px;height:9px;font-size:2.6px;padding:2px">Your name</div>
      <div class="field" style="left:81px;top:24px;width:50px;height:9px;font-size:2.6px;padding:2px">Your surname</div>
      <div class="field" style="left:28px;top:36px;width:50px;height:9px;font-size:2.6px;padding:2px">Email address</div>
      <div class="field" style="left:81px;top:36px;width:50px;height:9px;font-size:2.6px;padding:2px">Phone#</div>
      <div class="field" style="left:28px;top:48px;width:103px;height:25px;font-size:2.6px;padding:2px">Message
        <span class="abs" style="right:3px;bottom:3px;background:var(--btn-grey);font-style:normal;font-size:2px;padding:1px 2px">Upload Resume</span></div>
      <div class="btn grey" style="left:28px;top:77px;width:37px;height:8px;font-size:2.4px;line-height:8px">SUBSCRIBE</div>
    </section>
    <section style="height:100px;text-align:center">
      <div style="font-size:5.5px;font-weight:500;letter-spacing:.8px;margin-top:9px">FEATURE <span class="blue">CANDIDATES</span></div>
      <svg class="abs" style="left:6px;top:40px" width="8" height="8" viewBox="0 0 13 13" fill="none" stroke="#777"><circle cx="6.5" cy="6.5" r="6"/><path d="M8 4L5.5 6.5 8 9"/></svg>
      <svg class="abs" style="left:145px;top:40px" width="8" height="8" viewBox="0 0 13 13" fill="none" stroke="var(--blue)"><circle cx="6.5" cy="6.5" r="6"/><path d="M5 4l2.5 2.5L5 9"/></svg>
      <div class="avatar" style="left:24px;top:29px;width:31px;height:31px;border-width:2px" role="img" aria-label="Candidate portrait"></div>
      <div class="avatar" style="left:64px;top:29px;width:31px;height:31px;border-width:2px" role="img" aria-label="Candidate portrait"></div>
      <div class="avatar" style="left:102px;top:29px;width:31px;height:31px;border-width:2px" role="img" aria-label="Candidate portrait"></div>
      <div class="abs" style="left:18px;top:65px;width:44px;font-size:2.4px">Liam Carter<br><span class="blue">Designation</span></div>
      <div class="abs" style="left:58px;top:65px;width:44px;font-size:2.4px">Noah Patel<br><span class="blue">Designation</span></div>
      <div class="abs" style="left:96px;top:65px;width:44px;font-size:2.4px">Evan Brooks<br><span class="blue">Designation</span></div>
      <div class="btn" style="left:58px;top:83px;width:44px;height:8px;font-size:2.3px;line-height:8px">VIEW ALL CANDIDATES</div>
    </section>
    <footer>
      <div class="abs" style="left:8px;top:11px;font-size:5px;font-weight:500">BrightHire</div>
      <p class="abs" style="left:8px;top:22px;width:140px;font-size:2.4px;line-height:1.3">Lorem Ipsum is simply dummy text of the printing and typesetting industry. Lorem Ipsum has been the industry's standard dummy text ever since the 1500s.</p>
      <svg class="abs" style="left:18px;top:34px" width="40" height="5" viewBox="0 0 40 5" fill="#fff"><circle cx="2" cy="2.5" r="1.8"/><circle cx="11" cy="2.5" r="1.8"/><circle cx="20" cy="2.5" r="1.8"/><circle cx="29" cy="2.5" r="1.8"/></svg>
      <div class="abs" style="left:8px;top:49px;font-size:5px;font-weight:500;line-height:1.6">Quick Links<br>Useful Info..<br>Contact us</div>
      <svg class="abs" style="right:6px;top:50px" width="6" height="22" viewBox="0 0 6 22" fill="none" stroke="#fff" stroke-width=".5"><circle cx="3" cy="3" r="2.5"/><circle cx="3" cy="11" r="2.5"/><circle cx="3" cy="19" r="2.5"/><path d="M2.3 2l1 1-1 1M2.3 10l1 1-1 1M2.3 18l1 1-1 1"/></svg>
      <div class="abs" style="left:0;right:0;top:92px;text-align:center;font-size:2.3px;line-height:1.6">Copyright © 2019 BrightHire, All Rights Reserved<br>Privacy Policy · Terms &amp; Conditions</div>
    </footer>
  </main>

</div>
</body>
</html>
```